Event partnership Brochure for Thames Arc Bout Evening

I have attached a version of what I want in French, I now want it redesigned with the writing in English (which I can supply all the text below) so no translating necessary, just insert my text in English and add it to the design with some extra pie charts & graphs from P3. I will supply all additional photographs & event partners logos by email. The general style should be similar to the brochure supplied by me here in the attachments.

TEXT
P1
Image & Name of each main event fighter and weight
Thames Arc Bout Evening

A Contest For the Super-middleweight Title of the Southern Area
Kennard Bostock (Pellow Rise) v Gideon Marlowe (Harlow) & pics of 4 main fighters 10rds

On Friday 2nd October 2015, London's Varnford Hall will be the stage for championship boxing. Kennard Bostock will take on Harlow's Gideon Marlowe for the British Southern Area Super-Middleweight Title.

Graphics of each event partner & sponsor Tixora, Brimstoke, Thames Arc, Vanguards, Quayford Harbour Prime

At bottom of page, 'Sponsorship Information Pack'

P2
Images of Venue 3 (-2 at top & 1 at bottom).

London's own television channel, 'Thames Arc', will be broadcasting 10 of leading promoter Dougie Prandle's 'Brimstoke Bout Evenings' over the coming 12 months.

The first event will mark the long awaited return of regular free-to-air boxing on television and offer all associated parties a premium branding opportunity over a number of media platforms.

This event will primarily showcase a Southern Area title fight, involving two London based boxers, and will be the inaugural 'Thames Arc Bout Evening'. The main broadcast events will be supported by a full bill of boxing featuring a host of up-and-coming boxers from the capital city.

A live broadcast will be aired on 'Thames Arc' at peak viewing times (Fridays and Saturdays, 8pm-10pm or 9pm-11pm) with repeat and 'on demand' showings over the following 28 days. In addition to this much of the undercard (supporting contests) will be broadcast as part of the popular RNGX series on network 8. The main events will also be broadcast internationally on a number of channels worldwide in Africa, Europe and North America.

Thames Arc is London’s first TV channel, offering Londoners the latest in arts, news, current affairs and events. Since being launched on 31st March 2014, Thames Arc has shown 15 months of consistent growth across the key measures of reach and share of viewing and was watched by 2.3 million Londoners in July 2015, that's 24% of all Londoners. In the same month Thames Arc outperformed many channels in London, to mention a few:- Bigger than Jester Junction, ELK, Bolt, Vista Meridian and Pathfinder. Thames Arc's weekly reach is about the same size as Plenary Audio' which is the 5th biggest London station in terms of weekly reach, The 960k weekly reach is more than twice as big as MRN Capital 97.3 and higher than the combined reach of QJR, Metro Surge and Amber. Thames Arc is owned by NWVK which is 100% owned by Korvath Holdings.

A hidden gem in the London entertainment scene, Brimstoke Bout Evenings are at the forefront of a boxing revolution. With a reputation for evenly matched fights between boxers that the public want to see, diehard fans and casual spectators alike can relish this unmissable experience.
Previous events have even been televised on Pantasport, RQTV, Network 8 and RingRealm, which just goes to show the high demand for these exciting fight cards.

As well as superbly matched fights, Brimstoke Bout Evenings are renowned for their all-round entertainment and VIP guest lists, making Brimstoke Bout Evenings incredibly popular, with high viewing figures across all platforms.

Tickets will go on sale to the public on Tuesday 1st September 2015 and are available through Brimstoke Boxing's official ticketing supplier Tixora priced £60 ringside and £35 unreserved seating. Events are normally 'sold out' well in advance.

P3
Image viewer % chart & share of viewership pie chart & number of anticipated viewers chart
Viewing data
Thames Arc has enjoyed 18 months of continual growth in viewing numbers and viewer share.
Viewer & social media demographic
66% of tickets sold to people living inside the M25
78% of our social media following is male
Ages of viewers 13-17 = 2.5%, 18-24 = 16.8%, 25-34 = 46.3%, 35-44 = 19.8%, 45-54 = 8.4%, 55-64 = 3.4% 65+ =2.8%

Brimstoke Boxing has a history of marketing its events successfully, achieving high viewing figures whichever platform it has been on, including;
Scoring the highest viewing audience for boxing of the year on Pellam TV in 2011
2nd highest on Pantasport 2011
2nd highest on Pantasport in 2012
In 2014 Brimstoke's live February Pantasport event drew 270,000 viewers.

P4
Graphic (central) depicting the media plan

5 sections
Media Opportunities

Press
2 press conferences per event (20 per season)
National and Pan European press coverage
Articles featured in Daily Courier?

2) Signage
Signage around the venue 500 posters distributed around London in various sites, pubs, cafes, sports clubs and restaurants.

3) Digital
Home page and banner on the home page of www.brimstokeboxing.example
Signage around the ring and fight venue to be placed on-line
Editorial (written and photographic) coverage of the event in the boxing press
Inclusion in social media campaigns on Chatterbook, Chirpline, Snapgrid directed at Brimstoke Boxing's 53K 'Friends' and 'Followers'
CRM on VidRiver & ClipStream.example
Signage on the event literature (tickets, posters, souvenir program)
Press conference back drop
Weigh in backdrop
Re-runs of main event and undercard fights
Branding on teasers trailers & pre-fight interview backdrops
Thames Arc coverage of the weigh-in
Sponsors logos to feature on all online advertising (campaigns on Chatterbook & Chirpline)

4) Television
Televised MC's announcements on Thames Arc
'Ringside Chatter' Twenty minute magazine style show to build interest in the forthcoming live event
2 hour live broadcast of the sporting action with commentary and post fight interviews
Footage from press conference
Footage from pre & post fight interviews
Footage from weigh-in
2 hour live broadcast on 'Thames Arc' and several re-runs on the same channel with additional Highlights shown on RNGX ('Network 9' & 'Eight') after 30 days
Magazine show

P6)
Sponsorship signage spaces
Graphic depicting ring with all possible sponsorship spaces.
3 boxing photographs across the bottom
Ring posts A, B, C, D,
Wedgelet cushions 1, 2, 3, 4, 5, 6, 7, 8
Ring rope straps A, B, C, D, E, F, G, H
Advertising slots in the ring 1, 2, 3, 4, 5

Media
'Media' 'Volume' 'Value'
20 Trailers on 'Thames Arc' TV station £5,000
Distribution of press conference footage (2 press conferences per even- includes interviews etc) £5,000
Weigh in footage broadcast on Thames Arc £5,000
Banner on BrimstokeBoxing.example £2,000
Press articles released daily in London, UK and sporting press £5,000
Signage and mentions throughout 2 hour ThamesArc peak hours 2 hour live broadcast £30,000
Signage and mentions throughout re-runs of main events and undercard £15,000
Broadcast of summarisation of events £5,000
Signage on post fight interviews £5,000
Public workout £5,000
Articles in press in all media £5,000
CRM & video on ClipStream, VidRiver £5,000
Display advertising, value of all methods united £92,000

P7
Amber sponsorship package
£60,000
Central branding signage on ringmatt
Signage on 2 cornerposts
Branding on one of the ring ropes
Signage in corners on ringmatt
Presence of logo on all media
Presence and participation at event promotional meetings
Tickets per event -15 front row ringside
10 ringside
50 unreserved seating
Hospitality VIP Access
Cocktail +25 VIP bracelets

Silver sponsorship package
£35,000
Signage on 1 corner post
Signage on 'Wedgelet' cushions
Presence of logo at press conferences

Tickets per event
8 front row tickets
4 ringside tickets
30 unreserved seating
Hospitality VIP Access
Cocktail +12 VIP bracelets

Bronze sponsorship package
£20,000
Tickets per event 4 front row ringside tickets
4 ringside enclosure tickets
20 unreserved seating tickets
Cocktail & 8 VIP Bracelets

P8
Picture of wrapped fighters hands

Target Market(s)

Sponsors and advertisers

Industry/Entity Type

Advertising

Font styles to use
Sans Serif

Colors
ec1f27

Requirements
Must have
• Must look bright and exciting as well as being clear
Nice to have
• Bright and energatic

```html
<!DOCTYPE html>
<html lang="en">
<head>
<meta charset="utf-8">
<title>Thames Arc Bout Evening – Sponsorship Information Pack</title>
<link rel="stylesheet" href="https://fonts.googleapis.com/css2?family=Cinzel:wght@400;700&family=Oswald:wght@500;700&family=Roboto+Condensed:wght@400;700&display=swap">
<style>
  :root {
    --ink: #000000;
    --red: #ec1f27;
    --white: #ffffff;
    --smoke: #9a9a9a;
    --navy: #1d2a5c;
  }
  * { box-sizing: border-box; margin: 0; padding: 0; }
  html, body { width: 851px; height: 1200px; overflow: hidden; background: var(--ink); }
  .cover {
    position: relative;
    width: 851px;
    height: 1200px;
    background: var(--ink);
    color: var(--white);
    font-family: "Roboto Condensed", Arial, sans-serif;
  }
  .frame {
    position: absolute;
    left: 34px; top: 34px;
    width: 783px; height: 1080px;
    border: 2px solid var(--red);
  }
  .event-title {
    position: absolute;
    top: 118px; left: 0; width: 100%;
    text-align: center;
    font-family: "Cinzel", Georgia, serif;
    font-weight: 700;
    color: var(--red);
    line-height: 1.2;
  }
  .event-title .line-1 { display: block; font-size: 38px; letter-spacing: 1px; }
  .event-title .line-2 { display: block; font-size: 30px; letter-spacing: 1px; }
  .bout-title {
    position: absolute;
    top: 255px; left: 0; width: 100%;
    text-align: center;
    line-height: 1.15;
  }
  .bout-title .weight { display: block; font-size: 30px; font-weight: 700; color: var(--red); }
  .bout-title .belt { display: block; font-size: 22px; color: var(--white); letter-spacing: 0.5px; }

  .fight-photo {
    position: absolute;
    left: 36px; top: 330px;
    width: 779px; height: 540px;
    overflow: hidden;
  }
  .venue-backdrop {
    position: absolute; inset: 0 0 180px 0;
    background: linear-gradient(180deg, #1a1a1a 0%, #6e6e6e 45%, #8b8b8b 100%);
  }
  .flag-band {
    position: absolute; left: 0; right: 0; bottom: 0; height: 220px;
    background: linear-gradient(180deg, #2a0608 0%, #a3141b 40%, var(--navy) 75%, #000 100%);
  }
  .fighter {
    position: absolute; bottom: 40px;
  }
  .fighter-left {
    left: 0; width: 360px; height: 500px;
    background: radial-gradient(ellipse at 45% 45%, #6b4232 0%, #3b2219 55%, rgba(0,0,0,0) 80%);
  }
  .fighter-right {
    right: 0; width: 340px; height: 450px;
    background: radial-gradient(ellipse at 55% 45%, #d2a488 0%, #8d6552 50%, rgba(0,0,0,0) 80%);
  }
  .matchup {
    position: absolute; inset: 0;
    font-family: "Oswald", Impact, sans-serif;
    font-weight: 700;
    text-transform: uppercase;
    color: var(--white);
    text-shadow: 2px 2px 4px rgba(0,0,0,0.85);
  }
  .boxer { position: absolute; line-height: 1.05; }
  .boxer .name { display: block; font-size: 36px; }
  .boxer .home { display: block; font-size: 28px; font-weight: 500; }
  .boxer-red { left: 142px; top: 188px; }
  .boxer-red .home { padding-left: 60px; }
  .boxer-blue { left: 448px; top: 290px; text-align: right; }
  .versus { position: absolute; left: 395px; top: 264px; font-size: 34px; }

  .fight-date {
    position: absolute;
    top: 876px; left: 0; width: 100%;
    text-align: center;
    font-family: "Cinzel", Georgia, serif;
  }
  .fight-date .day {
    display: inline-block;
    font-size: 34px;
    padding: 6px 14px 4px;
    border-top: 1px solid var(--white);
    border-bottom: 1px solid var(--white);
  }
  .fight-date .venue {
    display: block;
    margin-top: 12px;
    font-family: "Roboto Condensed", Arial, sans-serif;
    font-size: 24px;
    letter-spacing: 1px;
    text-transform: uppercase;
  }
  .partners {
    position: absolute;
    top: 1002px; left: 0; width: 100%;
    display: flex; justify-content: center; gap: 14px;
    list-style: none;
  }
  .partner {
    display: flex; align-items: center; gap: 5px;
    font-size: 12px; font-weight: 700;
    color: var(--white);
  }
  .partner::before {
    content: ""; width: 10px; height: 10px; background: var(--white);
  }
  .pack-label {
    position: absolute;
    top: 1146px; left: 0; width: 100%;
    text-align: center;
    font-family: "Cinzel", Georgia, serif;
    font-size: 22px;
    letter-spacing: 3px;
    text-transform: uppercase;
  }
</style>
</head>
<body>
<main class="cover">
  <div class="frame"></div>

  <h1 class="event-title">
    <span class="line-1">THAMES ARC</span>
    <span class="line-2">BOUT EVENING</span>
  </h1>

  <h2 class="bout-title">
    <span class="weight">SUPER-MIDDLEWEIGHT</span>
    <span class="belt">TITLE OF THE SOUTHERN AREA</span>
  </h2>

  <section class="fight-photo">
    <div class="venue-backdrop" role="img" aria-label="Grey photograph of the venue building behind the fighters"></div>
    <div class="flag-band" role="img" aria-label="Waving British flag across the lower band"></div>
    <div class="fighter fighter-left" role="img" aria-label="Kennard Bostock posing with raised gloves"></div>
    <div class="fighter fighter-right" role="img" aria-label="Gideon Marlowe posing with gloves and title belt"></div>
    <div class="matchup">
      <p class="boxer boxer-red"><span class="name">Kennard Bostock</span><span class="home">(Pellow Rise)</span></p>
      <p class="versus">VS</p>
      <p class="boxer boxer-blue"><span class="name">Gideon Marlowe</span><span class="home">(Harlow)</span></p>
    </div>
  </section>

  <div class="fight-date">
    <span class="day">FRIDAY 2ND OCTOBER 2015</span>
    <span class="venue">London's Varnford Hall</span>
  </div>

  <ul class="partners">
    <li class="partner">Tixora</li>
    <li class="partner">Brimstoke</li>
    <li class="partner">Thames Arc</li>
    <li class="partner">Vanguards</li>
    <li class="partner">Quayford Harbour Prime</li>
  </ul>

  <p class="pack-label">Sponsorship Information Pack</p>
</main>
</body>
</html>
```